First and Only Single Serving Dental Tooth Powder Company NEEDS Packaging DESIGN

We need a packaging design for a new company based in Florida called 'ZunoDab'. We created the first and only single serving dental tooth powder, for use with or without water. This solves a world problem in numerous faucets. Our product is great for Travelers, Adventure Seekers, Military Personnel, Daily Commuters and any one else wanting the cleanest mouth and freshest breath.

- This is a front and back of a 4(four) by 6(six) package design needed

Target Market(s)

Travelers,Outdoorsman, Adventure seekers, Daily Commuters, and Military Personnel.

Industry/Entity Type

Dental

Requirements
Must have
• -This must fit a package with the dimensions of 4" x 6"
• -four inches by six inches.
• -Earthy/Naturalistic Appeal
• - This is a front and back of a 4(four) by 6(six) package design needed
• -The package will be a White Nylon/Mylar bag
Nice to have
• -Clean your teeth anywhere, anytime...
• -Simple, Convenient, Effective
• -ZunoDab activates without water
• -Proudly made in the USA.
• -Package contains 15 ZunoDab's.
• -The Flavor for the ZunoDab is "Velmo Plum"
• -ZunoDab is for the everyday person on-the-go.
• -Our Story..
• Zunodab was brought to life for moments when time is vital and packing light is a must. We were tired of the same old ordinary way of cleaning our teeth while outdoors, on our adventures, or traveling the globe. The old way required water for it's use which isn't always readily available. With ZunoDab, water is not necessary. The package you hold in your hand contains no ordinary product. In fact, the way you use it is extremely unique and simple.
• Directions: Rip, Pour, Swish, Dispense. Enjoy your adventure responsibly!
Should not have
• A bunch of clutter besides that I am open to ideas.

```html
<!DOCTYPE html>
<html lang="en">
<head>
<meta charset="utf-8">
<title>ZunoDab Package – Front and Back</title>
<link href="https://fonts.googleapis.com/css2?family=Signika:wght@400;500;600;700&family=Roboto+Condensed:ital,wght@0,300;1,700&display=swap" rel="stylesheet">
<style>
  :root {
    --backdrop: #cbcbcb;
    --brand-green: #17733a;
    --white: #ffffff;
    --ink: #111111;
    --sky: #f7fafb;
    --haze: #b9cfd9;
    --ridge: #5d7686;
    --slope: #465a3a;
    --valley: #2c3a26;
    --flag-red: #c7464d;
    --flag-blue: #3a4a86;
    --flag-light: #eef0f4;
  }
  * { box-sizing: border-box; margin: 0; padding: 0; }
  html, body { width: 1200px; height: 1200px; overflow: hidden; }
  body {
    background: var(--backdrop);
    position: relative;
    font-family: "Signika", sans-serif;
  }
  .package-panel {
    position: absolute;
    top: 167px;
    width: 545px;
    height: 817px;
    overflow: hidden;
    color: var(--white);
  }
  .package-front { left: 36px; }
  .package-back { left: 619px; }
  .landscape-photo {
    position: absolute;
    inset: 0;
    background: linear-gradient(180deg,
      var(--white) 0%,
      var(--sky) 18%,
      var(--haze) 30%,
      var(--ridge) 45%,
      #4d6370 58%,
      var(--slope) 72%,
      var(--valley) 100%);
  }
  .brand-wordmark {
    position: absolute;
    left: 0; right: 0;
    text-align: center;
    font-family: "Signika", sans-serif;
    font-weight: 700;
    color: var(--brand-green);
    letter-spacing: 1px;
  }
  .package-front .brand-wordmark { top: 215px; font-size: 74px; }
  .package-back .brand-wordmark { top: 218px; font-size: 50px; }

  .headline-lead {
    position: absolute;
    left: 40px; top: 410px;
    font-family: "Roboto Condensed", sans-serif;
    font-weight: 300;
    font-size: 38px;
    text-shadow: 0 1px 3px rgba(0,0,0,.4);
  }
  .headline-emphasis {
    position: absolute;
    left: 52px; top: 456px;
    font-family: "Roboto Condensed", sans-serif;
    font-weight: 700;
    font-style: italic;
    font-size: 36px;
    letter-spacing: 1px;
    text-shadow: 0 1px 3px rgba(0,0,0,.4);
  }
  .tagline-quote {
    position: absolute;
    left: 60px; width: 400px; top: 526px;
    text-align: center;
    font-weight: 500;
    font-size: 25px;
    line-height: 32px;
    text-shadow: 0 1px 3px rgba(0,0,0,.5);
  }
  .origin-badge {
    position: absolute;
    left: 22px; top: 693px;
    width: 170px; height: 100px;
    border-radius: 10px;
    background: linear-gradient(150deg,
      var(--flag-blue) 0%,
      #7d87b2 30%,
      var(--flag-light) 50%,
      #e3a3a7 72%,
      var(--flag-red) 100%);
    box-shadow: 0 2px 6px rgba(0,0,0,.25);
  }
  .origin-badge-text {
    position: absolute;
    left: 22px; top: 721px;
    width: 170px;
    text-align: center;
    font-size: 17px;
    line-height: 20px;
    font-weight: 500;
    color: var(--ink);
    text-shadow: 0 0 3px var(--white), 0 0 3px var(--white), 0 0 2px var(--white);
  }
  .count-label {
    position: absolute;
    left: 200px; top: 739px;
    width: 138px; height: 37px;
    background: var(--white);
    border-radius: 6px;
    color: var(--brand-green);
    font-weight: 500;
    font-size: 24px;
    line-height: 37px;
    text-align: center;
  }
  .water-free-badge {
    position: absolute;
    left: 372px; top: 605px;
    width: 128px; height: 184px;
    background: radial-gradient(circle at 40% 30%, var(--white) 0%, #e6e9ec 100%);
    border-radius: 44px 44px 30px 30px;
  }
  .water-free-text {
    position: absolute;
    left: 366px; top: 630px;
    width: 140px;
    text-align: center;
    color: var(--brand-green);
    font-weight: 600;
    font-size: 19px;
    line-height: 20px;
  }
  .story-heading {
    position: absolute;
    left: 0; right: 0; top: 355px;
    text-align: center;
    color: var(--brand-green);
    font-weight: 700;
    font-size: 23px;
    text-shadow: 0 0 2px var(--white), 0 0 2px var(--white);
  }
  .story-body {
    position: absolute;
    left: 0; right: 0; top: 394px;
    text-align: center;
    font-weight: 500;
    font-size: 17.5px;
    line-height: 20.5px;
    text-shadow: 0 1px 3px rgba(0,0,0,.5);
  }
  .story-directions {
    position: absolute;
    left: 0; right: 0; top: 662px;
    text-align: center;
    font-weight: 500;
    font-size: 17.5px;
    line-height: 20.5px;
    text-shadow: 0 1px 3px rgba(0,0,0,.5);
  }
</style>
</head>
<body>
  <section class="package-panel package-front">
    <div class="landscape-photo" role="img" aria-label="Photo of misty mountain peaks above a green alpine valley under a pale sky"></div>
    <div class="brand-wordmark">ZUNODAB</div>
    <p class="headline-lead">Brush your teeth</p>
    <p class="headline-emphasis">ANYTIME, ANYWHERE...</p>
    <p class="tagline-quote">“ZunoDab is for the<br>everyday person on-the-go.”</p>
    <div class="origin-badge" role="img" aria-label="Waving American flag illustration"></div>
    <p class="origin-badge-text">Proudly made<br>in the USA.</p>
    <div class="count-label">30 Sticks</div>
    <div class="water-free-badge" role="img" aria-label="Glossy white tooth illustration"></div>
    <p class="water-free-text">ZunoDab<br>ACTIVATES<br>Without<br>Water!</p>
  </section>

  <section class="package-panel package-back">
    <div class="landscape-photo" role="img" aria-label="Photo of misty mountain peaks above a green alpine valley under a pale sky"></div>
    <div class="brand-wordmark">ZUNODAB</div>
    <h2 class="story-heading">OUR STORY</h2>
    <p class="story-body">
      Zunodab was brought to life for the moments<br>
      when time is vital and packing light is a must.<br>
      We were tired of the same old ordinary way<br>
      of brushing our teeth while outdoors,<br>
      on our adventures, or while traveling the globe.<br>
      The old way required water for its use which<br>
      isn't always readily available.<br>
      With ZunoDab water is of no need.<br>
      The package you hold in your hand is no ordinary<br>
      product. In fact, the way you use it is<br>
      extraordinarily simple and its for extraordinary<br>
      people just like you!
    </p>
    <p class="story-directions">
      Rip, Pour, Swish, Dispense.<br>
      Enjoy your adventure responsibly!
    </p>
  </section>
</body>
</html>
```